Sudden Tides "Lantern Road" New Single Cover

Create cover artwork for the band Sudden Tides' new single "Lantern Road" being released early 2020. Style, font and graphics to be consistent with band's previous releases and overall brand identity. Visit www.suddentidesband.example and our Spotify page https://music.example.net/artist/7QzWpLx3RtVnKd8e2YbHcJ?si=MUrTgKa4PLe7skvWq2AmZd to view our previous releases and overall brand identity. Some examples attached as well. We are looking for someone to work with on future projects as well.

Lyrics are here: https://docs.example.org/document/d/3KTp9wrn_2ZQa8eXb4Lo_fimH7C5m83Jz4Pd70hrtVcA/edit

Music is here: https://audiostream.example.com/suddentides/lantern-road/s-pzkwa

Font styles to use
Sans Serif

Colors

Designer to choose colors to be used in the design.

Requirements
Must have
• Must be consistent with current brand identity and with prior album / single art.

```html
<!DOCTYPE html>
<html lang="en">
<head>
<meta charset="utf-8">
<title>Sudden Tides — Lantern Road</title>
<link rel="stylesheet" href="https://fonts.googleapis.com/css2?family=Josefin+Sans:wght@200;300&display=swap">
<style>
  :root {
    --sky-top: #fcf7a2;
    --sky-soft: #f7ef6c;
    --sky-mid: #eee21c;
    --sky-deep: #d6c611;
    --sky-base: #857a08;
    --ink: #0b0b05;
    --paper: #ffffff;
    --sun-core: #e9da1a;
    --sun-edge: rgba(233, 218, 26, 0);
  }
  html, body {
    margin: 0;
    padding: 0;
    width: 1200px;
    height: 1200px;
    overflow: hidden;
    background: var(--sky-top);
  }
  .cover {
    position: relative;
    width: 1200px;
    height: 1200px;
    background: linear-gradient(180deg,
      var(--sky-top) 0%,
      var(--sky-soft) 30%,
      var(--sky-mid) 55%,
      var(--sky-deep) 76%,
      var(--sky-base) 100%);
    font-family: "Josefin Sans", "Futura", sans-serif;
  }
  .cover-art {
    position: absolute;
    inset: 0;
    width: 1200px;
    height: 1200px;
  }
  .title-word {
    fill: var(--ink);
    font-weight: 300;
  }
  .title-across { font-size: 262px; }
  .title-down { font-size: 212px; }
  .band-name {
    fill: var(--paper);
    font-weight: 300;
    font-size: 92px;
  }
</style>
</head>
<body>
  <main class="cover">
    <svg class="cover-art" viewBox="0 0 1200 1200" xmlns="http://www.w3.org/2000/svg">
      <defs>
        <radialGradient id="sun-glow" cx="50%" cy="50%" r="50%">
          <stop offset="0%" stop-color="var(--sun-core)"/>
          <stop offset="60%" stop-color="var(--sun-core)" stop-opacity="0.6"/>
          <stop offset="100%" stop-color="var(--sun-edge)"/>
        </radialGradient>
      </defs>

      <text class="title-word title-across" x="118" y="306"
            textLength="960" lengthAdjust="spacingAndGlyphs">LANTERN</text>

      <g class="title-word title-down" text-anchor="middle">
        <text x="990" y="512">R</text>
        <text x="990" y="700">O</text>
        <text x="990" y="886">A</text>
        <text x="990" y="1072">D</text>
      </g>

      <circle class="sun-emblem" cx="592" cy="600" r="186" fill="url(#sun-glow)"
              role="img" aria-label="Line-drawn radiant sun emblem"/>

      <g class="band-name">
        <text x="126" y="962">SUDDEN</text>
        <text x="126" y="1078">TIDES</text>
      </g>
    </svg>
  </main>
</body>
</html>
```